Vemtra Group: Business Card for a high end technology company

We need a cool new design for our business cards using our cloud logo. We are a technology consulting business. We pride ourselves on be the best of the best. We mainly focus on cloud solutions and managed services. We need a business card that sets us apart from the other technology companies in the area and allows us to stand out.

Target Market(s)

Technology departments, CIO, CEOs, and Information Technology Staff.

Industry/Entity Type

Information Technology

Contact Information for Business Card

Must have the logo and our name.
Must have employee name, email address, office phone, cell phone and website.
Need to have all info on one side a cool design on backside.

Font styles to use
Serif
Sans Serif

Requirements
Must have
• Must have the logo and our name.
• Must have employee name, email address, office phone, cell phone and website.
• Need to have all info on one side a cool design on back side.
• Must be a crisp clean design, not too busy or confusing.

```html
<!DOCTYPE html>
<html lang="en">
<head>
<meta charset="utf-8">
<title>Vemtra Group — Stationery</title>
<link rel="stylesheet" href="https://fonts.googleapis.com/css2?family=Montserrat:wght@400;500&family=Open+Sans:wght@400;600&display=swap">
<style>
  :root {
    --blue-deep: #1556c9;
    --blue-mid: #2f8ff0;
    --blue-light: #7cc8ff;
    --ink: #1d1f24;
    --ink-soft: #3b3e45;
    --paper: #ffffff;
    --backdrop: #e9ebee;
    --rule: #9a9ea6;
    --window: #c9cbcf;
    --shadow: 0 6px 18px rgba(20, 30, 50, 0.18);
  }
  * { box-sizing: border-box; margin: 0; padding: 0; }
  html, body { width: 908px; height: 1200px; overflow: hidden; }
  body {
    position: relative;
    background: var(--backdrop);
    font-family: "Open Sans", Arial, sans-serif;
    color: var(--ink);
  }
  .sheet { position: absolute; background: var(--paper); box-shadow: var(--shadow); overflow: hidden; }

  .wordmark {
    display: flex; align-items: center; gap: 8px;
    font-family: "Montserrat", Arial, sans-serif; font-weight: 500;
    color: var(--ink); white-space: nowrap;
  }
  .wordmark .dot { width: 12px; height: 12px; border-radius: 50%; background: var(--blue-mid); flex: none; }
  .web { font-family: "Montserrat", Arial, sans-serif; font-weight: 500; color: var(--ink); }

  .ribbon { position: absolute; background: linear-gradient(135deg, var(--blue-deep), var(--blue-mid) 55%, var(--blue-light)); }

  /* Business card front */
  .card-front { left: 30px; top: 70px; width: 310px; height: 176px; }
  .card-front .lockup { position: absolute; left: 0; right: 0; top: 62px; display: flex; flex-direction: column; align-items: center; gap: 6px; }
  .card-front .wordmark { font-size: 26px; }
  .card-front .web { font-size: 8px; }

  /* Business card back */
  .card-back { left: 30px; top: 270px; width: 310px; height: 176px; }
  .card-back .ribbon { left: 0; top: 0; width: 120px; height: 36px; clip-path: polygon(0 0, 100% 0, 72% 100%, 48% 30%, 0 60%); }
  .card-back .wordmark { position: absolute; left: 60px; top: 66px; font-size: 22px; }
  .card-back .employee { position: absolute; right: 18px; top: 46px; font-family: "Montserrat", Arial, sans-serif; font-size: 8px; line-height: 1.5; text-align: left; }
  .card-back .address { position: absolute; left: 18px; top: 118px; font-family: "Montserrat", Arial, sans-serif; font-size: 7.5px; line-height: 1.5; }
  .card-back .contact { position: absolute; left: 160px; top: 116px; padding-left: 8px; border-left: 1px solid var(--ink); font-family: "Montserrat", Arial, sans-serif; font-size: 7.5px; line-height: 1.6; }

  /* Letterhead */
  .letterhead { left: 372px; top: 56px; width: 506px; height: 716px; }
  .letterhead .ribbon-corner { right: 0; top: 0; width: 150px; height: 170px; clip-path: polygon(0 0, 100% 0, 100% 100%, 78% 40%, 60% 0, 45% 55%); }
  .letterhead .wordmark { position: absolute; left: 56px; top: 120px; font-size: 22px; }
  .letterhead .web-line { position: absolute; left: 78px; top: 150px; font-size: 7px; }
  .letterhead .body { position: absolute; left: 56px; right: 56px; top: 238px; font-size: 7.6px; line-height: 1.38; color: var(--ink-soft); text-align: justify; }
  .letterhead .body p + p { margin-top: 8px; }
  .letterhead .ribbon-foot { left: 0; bottom: 70px; width: 130px; height: 110px; clip-path: polygon(0 20%, 30% 0, 60% 30%, 90% 10%, 100% 60%, 70% 100%, 0 100%); }
  .letterhead .signoff { position: absolute; right: 56px; top: 545px; text-align: right; font-size: 7px; color: var(--ink-soft); }
  .letterhead .signoff strong { display: block; margin-top: 3px; font-family: "Montserrat", Arial, sans-serif; font-size: 8px; color: var(--ink); }
  .letterhead .footer { position: absolute; left: 190px; bottom: 36px; font-family: "Montserrat", Arial, sans-serif; font-size: 9px; line-height: 1.6; color: var(--ink-soft); }

  /* Envelopes */
  .envelope-front { left: 34px; top: 820px; width: 410px; height: 205px; }
  .envelope-front .wordmark { position: absolute; left: 26px; top: 26px; font-size: 15px; }
  .envelope-front .wordmark .dot { width: 9px; height: 9px; }
  .envelope-front .web { position: absolute; left: 43px; top: 46px; font-size: 5px; }
  .envelope-front .window { position: absolute; left: 26px; top: 110px; width: 130px; height: 58px; border-radius: 6px; background: var(--window); }
  .envelope-front .ribbon { right: 0; top: 0; width: 80px; height: 205px; clip-path: polygon(60% 0, 100% 0, 100% 100%, 20% 90%, 50% 60%); }

  .envelope-back { left: 464px; top: 820px; width: 410px; height: 205px; }
  .envelope-back .ribbon-left { left: 0; top: 40px; width: 90px; height: 150px; clip-path: polygon(0 40%, 100% 0, 60% 100%, 20% 90%); }
  .envelope-back .ribbon-right { right: 0; top: 0; width: 60px; height: 205px; clip-path: polygon(0 0, 50% 0, 100% 100%, 55% 100%); }
</style>
</head>
<body>

  <section class="sheet card-front" aria-label="Business card, front">
    <div class="lockup">
      <div class="wordmark"><span class="dot"></span>Vemtra Group</div>
      <div class="web">www.vemtrahq.net</div>
    </div>
  </section>

  <section class="sheet card-back" aria-label="Business card, contact side">
    <div class="ribbon" role="img" aria-label="Blue gradient ribbon accent"></div>
    <div class="employee">Employee name<br>000.0000.0000</div>
    <div class="wordmark"><span class="dot"></span>Vemtra Group</div>
    <div class="address">482 Linden Row Suite 310<br>Marlow, GA 30412</div>
    <div class="contact">Phone: 555.218.0473<br>Email: hello@vemtrahq.net</div>
  </section>

  <section class="sheet letterhead" aria-label="Letterhead">
    <div class="ribbon ribbon-corner" role="img" aria-label="Blue gradient ribbon accent"></div>
    <div class="wordmark"><span class="dot"></span>Vemtra Group</div>
    <div class="web web-line">www.vemtrahq.net</div>
    <div class="body">
      <p>In dui turpis, varius vitae, tincidunt id, consequat ut, leo. Donec tincidunt tristique odio. Nulla erat felis, euismod nec, fringilla non, aliquet et, magna. Nulla at magna quis nisi pretium vehicula. Pellentesque habitant morbi tristique senectus et netus et malesuada fames ac turpis egestas. Class aptent taciti sociosqu ad litora torquent per conubia nostra, per inceptos himenaeos. In vel quam. Phasellus varius convallis purus. In non turpis. Nam sed risus. Etiam non neque at nisl gravida porttitor. Donec leo dolor, feugiat ut, pharetra et, porttitor a, metus.</p>
      <p>Nunc purus. Cras auctor. In ornare neque id ipsum. Nulla tincidunt, diam sit amet viverra euismod, sapien augue fringilla neque, at pellentesque felis tortor vel enim. Etiam dignissim. Sed a tortor imperdiet vel nisl euismod ultricies. Donec molestie congue lectus. Integer sed turpis a tortor imperdiet consequat. Maecenas molestie placerat urna. Sed pede enim, sollicitudin nec, pretium nec, sollicitudin a, felis. In hac habitasse platea dictumst.</p>
      <p>In dui turpis, varius vitae, tincidunt id, consequat ut, leo. Donec tincidunt tristique odio. Nulla erat felis, euismod nec, fringilla non, aliquet et, magna. Nulla at magna quis nisi pretium vehicula. Pellentesque habitant morbi tristique senectus et netus et malesuada fames ac turpis egestas. Class aptent taciti sociosqu ad litora torquent per conubia nostra.</p>
      <p>Nunc purus. Cras auctor. In ornare neque id ipsum. Nulla tincidunt, diam sit amet viverra euismod, sapien augue fringilla neque, at pellentesque felis tortor vel enim. Etiam dignissim. Donec molestie congue lectus. Sed pede enim, sollicitudin nec, pretium nec, sollicitudin a, felis. Vivamus tincidunt.</p>
    </div>
    <div class="signoff">Yours Sincerely,<strong>Dara Kellen</strong></div>
    <div class="ribbon ribbon-foot" role="img" aria-label="Blue gradient ribbon accent"></div>
    <div class="footer">482 Linden Row Suite 310, Marlow, GA 30412<br>Phone: 555.218.0473 • Email: hello@vemtrahq.net</div>
  </section>

  <section class="sheet envelope-front" aria-label="Envelope, front">
    <div class="wordmark"><span class="dot"></span>Vemtra Group</div>
    <div class="web">www.vemtrahq.net</div>
    <div class="window"></div>
    <div class="ribbon" role="img" aria-label="Blue gradient ribbon accent"></div>
  </section>

  <section class="sheet envelope-back" aria-label="Envelope, back">
    <div class="ribbon ribbon-left" role="img" aria-label="Blue gradient ribbon accent"></div>
    <div class="ribbon ribbon-right" role="img" aria-label="Blue gradient ribbon band"></div>
  </section>

</body>
</html>
```